Online Jewellery Marketing Design Project

I need a simple colour business card with a style that can easily be transferred into grayscale and can be used for as part of the design for brochures and gift certificates.

Design to revolve around Script, Peacock feathers and the colours found in them. I would also be open to a rich purple.

The business is a small discount online jewellery and painting sales. As business improves the designs will need to be able to be used on the card backings of the jewellery, a website with cart capability and other marketing tools.

The final design should communicate inexpensive style.

I have include some of the designs I have been using while this was just a hobby. Now that it is moving towards a proper business, even if only part time, a more professional touch is required.

Industry/Entity Type

Marketing

Logo Text

Mabel's Trinket Jewellery & Paintings

```html
<!DOCTYPE html>
<html lang="en">
<head>
<meta charset="utf-8">
<title>Mabel's Trinket – Business Card</title>
<link rel="stylesheet" href="https://fonts.googleapis.com/css2?family=Cabin:wght@500&display=swap">
<style>
  :root {
    --page-bg: #cfcfcf;
    --card-white: #ffffff;
    --ink: #4a4a4a;
    --logo-ink: #5a5a5a;
    --feather-navy: #27305e;
    --feather-blue: #3f5a85;
    --feather-teal: #5f8289;
    --feather-olive: #6f7a58;
    --feather-gold: #a8843f;
    --bevel: #b9b9b9;
  }
  * { margin: 0; padding: 0; box-sizing: border-box; }
  html, body {
    width: 1200px;
    height: 960px;
    overflow: hidden;
    background: var(--page-bg);
    font-family: "Cabin", "Gill Sans", sans-serif;
  }
  .card {
    position: absolute;
    width: 670px;
    height: 404px;
    overflow: hidden;
  }
  .card--front { left: 98px; top: 48px; }
  .card--back  { left: 420px; top: 511px; }

  .feather-field {
    position: absolute;
    inset: 0;
    background:
      radial-gradient(circle at 20% 30%, rgba(168,132,63,0.55) 0 6%, transparent 14%),
      radial-gradient(circle at 60% 45%, rgba(168,132,63,0.5) 0 6%, transparent 14%),
      radial-gradient(circle at 85% 15%, rgba(168,132,63,0.5) 0 5%, transparent 12%),
      radial-gradient(circle at 30% 80%, rgba(168,132,63,0.5) 0 6%, transparent 14%),
      radial-gradient(circle at 75% 75%, rgba(168,132,63,0.45) 0 5%, transparent 12%),
      linear-gradient(135deg, var(--feather-teal) 0%, var(--feather-navy) 30%, var(--feather-olive) 55%, var(--feather-blue) 80%, var(--feather-navy) 100%);
  }

  .front-panel {
    position: absolute;
    left: 46px;
    top: 38px;
    right: 0;
    bottom: 0;
    background: var(--card-white);
    border-top-left-radius: 62px;
    border-top: 3px solid var(--bevel);
    border-left: 3px solid var(--bevel);
  }

  .brand {
    position: absolute;
    color: var(--logo-ink);
    font-weight: 500;
    text-align: center;
    line-height: 1.1;
  }
  .brand--front {
    left: 380px;
    top: 108px;
    width: 260px;
  }
  .brand--front .brand-name { font-size: 34px; }
  .brand--front .brand-line { font-size: 20px; }

  .contact-list {
    position: absolute;
    left: 103px;
    top: 234px;
    list-style: none;
    color: var(--ink);
    font-size: 19px;
    font-weight: 500;
  }
  .contact-list li { height: 31px; line-height: 31px; }

  .back-corner {
    position: absolute;
    inset: 0;
  }
  .brand--back {
    left: 500px;
    top: 342px;
    width: 165px;
  }
  .brand--back .brand-name { font-size: 19px; }
  .brand--back .brand-line { font-size: 11px; }
</style>
</head>
<body>

  <section class="card card--front">
    <div class="feather-field" role="img" aria-label="Peacock feather pattern in navy, teal, olive and gold"></div>
    <div class="front-panel"></div>
    <div class="brand brand--front">
      <div class="brand-name">Mabel's Trinket</div>
      <div class="brand-line">Jewellery &amp; Paintings</div>
    </div>
    <ul class="contact-list">
      <li>www.Socialpage.com/MabelsTrinket</li>
      <li>www.Craftmarket.com/shop/MabelsTrinket</li>
      <li>myworld.auctionhub.com.au/mabel0412/</li>
      <li>MabelsTrinket@mailbox.com</li>
    </ul>
  </section>

  <section class="card card--back">
    <div class="feather-field" role="img" aria-label="Peacock feather pattern in navy, teal, olive and gold"></div>
    <svg class="back-corner" width="670" height="404" viewBox="0 0 670 404" aria-hidden="true">
      <path d="M434 404 Q560 340 670 317 L670 404 Z" fill="#ffffff"/>
    </svg>
    <div class="brand brand--back">
      <div class="brand-name">Mabel's Trinket</div>
      <div class="brand-line">Jewellery &amp; Paintings</div>
    </div>
  </section>

</body>
</html>
```